Orthopedic Arm Surgeon Brochure

Bifold modern design. I will supply the text, my photo, and photos of my textbooks. Prefer colors in the greens, blues, greys. For more information visit MendLimbWellCare.com Please feel free to e-mail me with any questions. Current brochure attached; I want to modernize this, get rid of frames, and change the text.

Target Market(s)

High-end market

Colors
3176b5
33a6d7
33b8a4
abd036
876aae
b768aa

Requirements
Must have
• Beautiful finishes
Should not have
• Bright reds, yellows, oranges that emit fear

```html
<!DOCTYPE html>
<html lang="en">
<head>
<meta charset="utf-8">
<title>Crestline Orthopedic Group – Bifold Brochure</title>
<link href="https://fonts.googleapis.com/css2?family=PT+Sans:wght@400;700&family=PT+Serif:wght@400;700&display=swap" rel="stylesheet">
<style>
:root{
  --backdrop:#d4d5d7;
  --paper:#ffffff;
  --paper-shade:#e9eaee;
  --green:#1f8a3a;
  --green-dark:#0f6a2a;
  --navy:#121638;
  --navy-mid:#1d2160;
  --pill:#2e3192;
  --pill-light:#4a4fb5;
  --ink:#3a3a3a;
  --ink-soft:#5a5a5a;
  --link:#1d2a9a;
  --sans:"PT Sans",Arial,sans-serif;
  --serif:"PT Serif",Georgia,serif;
}
*{box-sizing:border-box;margin:0;padding:0}
html,body{width:921px;height:1200px;overflow:hidden;background:var(--backdrop)}
.canvas{position:relative;width:921px;height:1200px;font-family:var(--sans);color:var(--ink)}
.page{position:absolute;width:388px;height:503px;overflow:hidden;
  background:linear-gradient(90deg,var(--paper-shade) 0%,var(--paper) 35%,var(--paper) 100%)}
.page.right{background:linear-gradient(270deg,var(--paper-shade) 0%,var(--paper) 35%,var(--paper) 100%)}
.spread-shadow{position:absolute;width:776px;height:503px;box-shadow:0 8px 10px -4px rgba(0,0,0,.35)}
.svg-layer{position:absolute;left:0;top:0}
.photo{position:absolute}
.ring{position:absolute;border-radius:50%;border:3px solid #fff;box-shadow:0 2px 6px rgba(0,0,0,.45)}

.phone-band{position:absolute;left:0;width:388px;height:26px;top:456px;background:var(--navy);
  color:#fff;font-size:15px;display:flex;align-items:center;justify-content:center;gap:6px}
.phone-band svg{width:13px;height:13px}
.site{position:absolute;left:0;width:388px;top:485px;text-align:center;font-size:11.5px;letter-spacing:.4px;color:var(--navy-mid)}

.brand{position:absolute;left:120px;top:22px;color:var(--green-dark);font-weight:700;font-family:var(--sans)}
.brand .line1{font-size:28px;letter-spacing:1px;line-height:30px}
.brand .line2{font-size:15px;line-height:18px;padding-left:4px}
.brand-dot{position:absolute;left:96px;top:28px;width:18px;height:18px;border-radius:50%;background:var(--green-dark)}
.joint{position:absolute;top:314px;width:64px;height:64px;border-radius:50%;border:2px solid #fff;
  background:radial-gradient(circle at 50% 45%,#4d8ee0 0%,#1b3e9e 55%,#0c1850 100%);box-shadow:0 2px 5px rgba(0,0,0,.4)}
.joint-label{position:absolute;top:384px;width:80px;text-align:center;font-size:8px;color:#444;letter-spacing:.3px}
.cover-name{position:absolute;left:0;width:388px;top:395px;text-align:center;font-family:var(--serif);font-size:20px;color:var(--navy-mid)}
.cover-role{position:absolute;left:0;width:388px;top:420px;text-align:center;font-size:13px;color:#1e1e1e}
.cover-list{position:absolute;left:0;width:388px;top:441px;text-align:center;font-size:7px;color:#555}

.book{position:absolute;width:50px;height:66px;box-shadow:1px 1px 3px rgba(0,0,0,.35)}
.bio-box{position:absolute;left:10px;top:236px;width:365px;height:134px;background:var(--navy);border-radius:5px;color:#fff;padding:8px 12px}
.bio-box h1{font-family:var(--serif);font-weight:400;font-size:14px;margin-bottom:6px;padding-bottom:5px;border-bottom:1px solid rgba(255,255,255,.25)}
.bio-box p{font-size:7px;line-height:10px;margin-bottom:6px}
.appt{position:absolute;left:14px;top:383px;font-size:9px;color:#222}
.appt b{font-weight:700}
.office{position:absolute;top:402px;font-size:7px;line-height:10px;color:#555}
.office svg{position:absolute;left:-11px;top:1px;width:6px;height:8px}

.pill{position:absolute;height:24px;border-radius:0 10px 0 10px;
  background:linear-gradient(180deg,var(--pill-light),var(--pill));color:#fff;font-size:12.5px;
  padding:4px 8px;box-shadow:0 1px 2px rgba(0,0,0,.3)}
.copy{position:absolute;font-size:6.4px;line-height:9.4px;color:var(--ink);text-align:justify}
.copy p{margin-bottom:6px}
.copy a{color:var(--link);font-weight:700;text-decoration:none}
.close-line{position:absolute;right:20px;color:#fff;text-align:right}
</style>
</head>
<body>
<div class="canvas">

  <div class="spread-shadow" style="left:69px;top:70px"></div>

  <section class="page" style="left:69px;top:70px">
    <svg class="svg-layer" width="388" height="503" viewBox="0 0 388 503">
      <path d="M0 0 H330 C230 22 110 60 0 150 Z" fill="#1f8a3a"/>
      <path d="M0 150 C110 60 230 22 330 0 H388 C250 20 120 70 0 168 Z" fill="#e8e9ec"/>
    </svg>
    <div class="photo" role="img" aria-label="Portrait of the surgeon in a dark suit"
      style="left:23px;top:66px;width:140px;height:172px;background:linear-gradient(180deg,#e9e9eb 0%,#c9c9cd 40%,#2b2b31 75%,#1a1a20 100%)"></div>

    <div class="book" role="img" aria-label="Textbook cover" style="left:158px;top:86px;background:linear-gradient(160deg,#d9b468,#8a6a2e)"></div>
    <div class="book" role="img" aria-label="Textbook cover" style="left:213px;top:86px;background:linear-gradient(160deg,#2d7ac7,#114f8f)"></div>
    <div class="book" role="img" aria-label="Textbook cover" style="left:268px;top:86px;background:linear-gradient(160deg,#f2f2f2,#2f5ea8)"></div>
    <div class="book" role="img" aria-label="Textbook cover" style="left:323px;top:86px;background:linear-gradient(160deg,#c98b3c,#3a2a55)"></div>
    <div class="book" role="img" aria-label="Textbook cover" style="left:183px;top:158px;background:linear-gradient(160deg,#7a4f2a,#4a2d17)"></div>
    <div class="book" role="img" aria-label="Textbook cover" style="left:243px;top:158px;background:linear-gradient(160deg,#2d2f6e,#191a3f)"></div>
    <div class="book" role="img" aria-label="Textbook cover" style="left:303px;top:158px;background:linear-gradient(160deg,#c4262d,#7d1116)"></div>

    <div class="bio-box">
      <h1>Daniel R. Whitcombe, MD</h1>
      <p>Dr. Whitcombe is a nationally-recognized Orthopedic Upper Extremity Surgeon who has edited 8 textbooks, published over 45 original research papers and written 23 textbook chapters.</p>
      <p>Dr. Whitcombe graduated Cum Laude from Harborview University and with honors from Eastbrook Medical School. He completed his residency in Orthopedic Surgery at the University of Westmont. In order to obtain expertise covering the entire upper extremity, he completed two fellowships, one in Hand Surgery and the other in Sports Medicine. He is Board Certified in Orthopedic Surgery and has a Subspecialty Certificate in Surgery of the Hand.</p>
    </div>

    <div class="appt">Appointments can be made online through <b>BookCareNow.com</b></div>

    <div class="office" style="left:25px">
      <svg viewBox="0 0 6 8"><path d="M3 0a3 3 0 0 1 3 3c0 2-3 5-3 5S0 5 0 3a3 3 0 0 1 3-3z" fill="#1f8a3a"/></svg>
      Medical District<br>2400 Linden Ave, Suite 410<br>Riverton, ST 00120<br>&#9990; 555-240-0118
    </div>
    <div class="office" style="left:122px">
      <svg viewBox="0 0 6 8"><path d="M3 0a3 3 0 0 1 3 3c0 2-3 5-3 5S0 5 0 3a3 3 0 0 1 3-3z" fill="#1f8a3a"/></svg>
      Westbrook<br>180 Park Row<br>Westbrook, ST 00141<br>&#9990; 555-240-0118
    </div>
    <div class="office" style="left:196px">
      <svg viewBox="0 0 6 8"><path d="M3 0a3 3 0 0 1 3 3c0 2-3 5-3 5S0 5 0 3a3 3 0 0 1 3-3z" fill="#1f8a3a"/></svg>
      Southfield<br>3280 Meadow<br>Dr., Suite 118<br>Southfield, ST 00158<br>&#9990; 555-240-0118
    </div>
    <div class="office" style="left:289px">
      <svg viewBox="0 0 6 8"><path d="M3 0a3 3 0 0 1 3 3c0 2-3 5-3 5S0 5 0 3a3 3 0 0 1 3-3z" fill="#1f8a3a"/></svg>
      Northgate<br>4620 Ridge Lane North<br>Northgate, ST 00173<br>&#9990; 555-240-0118
    </div>

    <div class="phone-band">
      <svg viewBox="0 0 14 14"><circle cx="7" cy="7" r="6.2" fill="none" stroke="#fff" stroke-width="1.2"/><path d="M4.6 3.8l1.3-.3.8 1.8-.8.6c.4.9 1.1 1.6 2 2l.6-.8 1.8.8-.3 1.3c-3 .2-5.6-2.4-5.4-5.4z" fill="#fff"/></svg>
      555-240-LIMB
    </div>
    <div class="site">www.MendLimbWellCare.com</div>
  </section>

  <section class="page right" style="left:457px;top:70px">
    <div class="photo" role="img" aria-label="Tennis player reaching for a ball on a green court"
      style="left:0;top:70px;width:388px;height:270px;background:linear-gradient(180deg,#8fb27e 0%,#5f8f4a 45%,#3d6b31 100%)"></div>
    <svg class="svg-layer" width="388" height="503" viewBox="0 0 388 503">
      <path d="M0 0 H388 V70 C260 78 120 98 0 140 Z" fill="#ffffff"/>
      <path d="M0 120 C120 90 260 78 388 72 V86 C260 92 130 108 0 142 Z" fill="#1f8a3a"/>
      <path d="M0 300 C120 330 260 330 388 290 V503 H0 Z" fill="#ffffff"/>
      <path d="M0 300 C120 330 260 330 388 290" fill="none" stroke="#121638" stroke-width="3"/>
    </svg>
    <div class="brand-dot"></div>
    <div class="brand"><div class="line1">CRESTLINE</div><div class="line2">Orthopedic Group, L.L.P.</div></div>

    <div class="joint" role="img" aria-label="Medical illustration of the hand" style="left:39px"></div>
    <div class="joint" role="img" aria-label="Medical illustration of the wrist" style="left:118px"></div>
    <div class="joint" role="img" aria-label="Medical illustration of the elbow" style="left:196px"></div>
    <div class="joint" role="img" aria-label="Medical illustration of the shoulder" style="left:275px"></div>
    <div class="joint-label" style="left:31px">HAND</div>
    <div class="joint-label" style="left:110px">WRIST</div>
    <div class="joint-label" style="left:188px">ELBOW</div>
    <div class="joint-label" style="left:267px">SHOULDER</div>

    <div class="cover-name">Daniel R. Whitcombe, MD</div>
    <div class="cover-role">Specialist in Surgery of the Hand, Wrist, Elbow &amp; Sholder</div>
    <div class="cover-list">Carpal Tunnel • Cubital Tunnel • Trigger Finger • DeQuervain's Tendinitis • Elbow &amp; Shoulder Pain</div>

    <div class="phone-band">
      <svg viewBox="0 0 14 14"><circle cx="7" cy="7" r="6.2" fill="none" stroke="#fff" stroke-width="1.2"/><path d="M4.6 3.8l1.3-.3.8 1.8-.8.6c.4.9 1.1 1.6 2 2l.6-.8 1.8.8-.3 1.3c-3 .2-5.6-2.4-5.4-5.4z" fill="#fff"/></svg>
      555-240-LIMB
    </div>
    <div class="site">www.MendLimbWellCare.com</div>
  </section>

  <div class="spread-shadow" style="left:69px;top:630px"></div>

  <section class="page" style="left:69px;top:630px">
    <div class="photo" role="img" aria-label="Football player diving for a catch in a stadium"
      style="left:0;top:0;width:388px;height:150px;background:linear-gradient(180deg,#3d78c4 0%,#9cbbe0 50%,#c9a9b0 100%)"></div>
    <svg class="svg-layer" width="388" height="503" viewBox="0 0 388 503">
      <path d="M0 120 C130 150 260 150 388 110 V503 H0 Z" fill="#f4f4f6"/>
      <path d="M0 120 C130 150 260 150 388 110" fill="none" stroke="#121638" stroke-width="4"/>
      <path d="M0 490 C150 486 280 480 388 476 V503 H0 Z" fill="#1f8a3a"/>
    </svg>
    <div class="ring" role="img" aria-label="Medical illustration of the elbow joint"
      style="left:283px;top:66px;width:82px;height:82px;background:radial-gradient(circle,#3b6fd0 0%,#142a7a 70%)"></div>

    <div class="pill" style="left:5px;top:180px;width:169px">Carpal Tunnel Syndrome</div>
    <div class="pill" style="left:195px;top:180px;width:169px">Cubital Tunnel Syndrome</div>

    <div class="copy" style="left:11px;top:211px;width:176px">
      <p>Carpal Tunnel Syndrome occurs when the main/median nerve to the hand gets pinched at the wrist. This leads to fingers feeling “numb”, “asleep”, “cold”, like they “lack circulation” or have “pins and needles” in them. Carpal tunnel syndrome is usually worst at night or upon awakening. If you wake up at night with your hand numb or painfully asleep, and have to “shake it out” to get relief, you've probably got carpal tunnel syndrome. Symptoms also often occur with gripping, such as when driving, writing or holding books, cell phones or tools.</p>
      <p>Unless the carpal tunnel syndrome has led to nerve damage, initial treatment often involves splinting the wrist at night when asleep. If that doesn't work, the carpal tunnel can be released. The least invasive technique is the Single-Incision Endoscopic Carpal Tunnel Release. This quick, minimally invasive, outpatient procedure uses a small incision at the wrist without any incision in the hand. Compared to other techniques, there is decreased pain and a quicker return to work and other activities. There are no bandages, and hand washing and showering can be performed immediately.</p>
      <p>To see a video of an Endoscopic Carpal Tunnel Release please go to: <a>www.MendLimbWellCare.com</a></p>
    </div>

    <div class="copy" style="left:202px;top:211px;width:176px">
      <p>Cubital tunnel syndrome occurs when the funny bone (ulnar) nerve gets pinched at the elbow. This leads to tingling and numbness of the small finger when the elbow is bent, usually at night or when talking on the phone. Numbness may also occur when the elbow is placed on a hard surface.</p>
      <p>Unless nerve damage has occurred, treatment starts with avoiding pressure on the elbow, and not resting the elbow on desks, arm rests, or other hard objects. Avoid prolonged elbow flexion: use the other hand to hold phones or get a hands-free device.</p>
      <p>If this fails, the least invasive definitive treatment is an Endoscopic Cubital Tunnel Release. This minimally invasive, outpatient procedure allows an early return to activities with a low complication rate. No splint is used after surgery.</p>
      <p>To see a video of an Endoscopic Cubital Tunnel Release please go to: <a>www.MendLimbWellCare.com</a></p>
    </div>
  </section>

  <section class="page right" style="left:457px;top:630px">
    <div class="photo" role="img" aria-label="Baseball batter swinging in a stadium"
      style="left:0;top:0;width:388px;height:140px;background:linear-gradient(180deg,#4a4f5c 0%,#8c8f96 50%,#b9b4a8 100%)"></div>
    <svg class="svg-layer" width="388" height="503" viewBox="0 0 388 503">
      <path d="M0 130 C130 116 260 112 388 122 V503 H0 Z" fill="#f4f4f6"/>
      <path d="M0 130 C130 116 260 112 388 122" fill="none" stroke="#121638" stroke-width="4"/>
      <path d="M0 490 C140 482 270 468 388 440 V503 H0 Z" fill="#1f8a3a"/>
      <path d="M0 494 C140 486 270 474 388 448 V503 H0 Z" fill="#0f6a2a"/>
    </svg>
    <div class="ring" role="img" aria-label="Medical illustration of the wrist and hand"
      style="left:270px;top:22px;width:84px;height:84px;background:radial-gradient(circle,#3b6fd0 0%,#142a7a 70%)"></div>

    <div class="pill" style="left:6px;top:135px;width:169px">Trigger Finger</div>
    <div class="copy" style="left:11px;top:164px;width:365px">
      <p>Trigger finger occurs when the tendon that moves the finger gets pinched in its tunnel. This causes the finger to get stuck or stiff, which is often worse in the morning. This catching or locking can be quite painful. Grip may also cause pain. The finger may occasionally get stuck straight and be difficult to bend.</p>
      <p>Splinting may temporarily prevent the catching, but doesn't actually treat the problem. If caught early, a steroid injection can be curative. After 4-6 months the chance of an injection permanently curing the condition is lower, but still often worth a try.</p>
      <p>If the triggering returns following an injection, the problem can be definitively treated with a minimally-invasive Trigger Finger Release. This highly successful outpatient surgery is almost always a permanent cure.</p>
      <p>To see a video of a Trigger Finger Release please go to: <a>www.MendLimbWellCare.com</a></p>
    </div>

    <div class="pill" style="left:6px;top:270px;width:169px">Wrist Pain</div>
    <div class="copy" style="left:11px;top:299px;width:365px">
      <p>Wrist pain may have many causes and the diagnosis is best made by a fellowship-trained Hand Surgeon. The most common cause is DeQuervain's tendinitis, which causes pain on the thumb side of the wrist. This occurs when the tendons to the thumb and wrist get pinched in their tunnel. Pain is usually worse with lifting and gripping.</p>
      <p>DeQuervain's Tendinitis is common in mothers who repetitively lift children. It can also occur following frequent lifting with the thumb up, such as when pulling weeds, luggage or moving heavy objects.</p>
      <p>Initial treatment is to avoid lifting with the thumb up. If lifting is necessary, lift with the palm up or the palm down. To lift small children, keep the palm up and 'scoop under' the child. Use the other hand to bear most of the weight. A single steroid injection often helps by decreasing inflammation in the tunnel. In mild cases, this can be curative, especially if the problem is treated early and stressful activities can be avoided. Unfortunately, sometimes there's a very small second tunnel that causes problems and doesn't respond well to injections.</p>
      <p>If the tendinitis recurs after injection, an outpatient tendon release is very effective. To prevent tendon subluxation after tunnel release, I lengthen the restraints that stabilize the tendon and repair them in a lengthened position.</p>
      <p>To see a video of a DeQuervain's Tendinitis Release please go to: <a>www.MendLimbWellCare.com</a></p>
    </div>

    <div class="close-line" style="top:462px;font-size:14px;display:flex;align-items:center;gap:5px">
      <svg viewBox="0 0 14 14" width="13" height="13"><circle cx="7" cy="7" r="6.2" fill="none" stroke="#fff" stroke-width="1.2"/><path d="M4.6 3.8l1.3-.3.8 1.8-.8.6c.4.9 1.1 1.6 2 2l.6-.8 1.8.8-.3 1.3c-3 .2-5.6-2.4-5.4-5.4z" fill="#fff"/></svg>
      555-240-LIMB
    </div>
    <div class="close-line" style="top:482px;font-size:9px">Appointments can be made online through <b>BookCareNow.com</b></div>
  </section>

</div>
</body>
</html>
```